Business Card Design Project - Zorvex Labs

High quality business card Must be funky.

We are an IT support from home and office, but our image is more retro.

Our logo is black and lime green. IT should be a 2 sided card with the multiple coloured ties somehow used on the reverse side (be creative!)

Black or white background fine or a combo of both

Target Market(s)

consumer and business

Industry/Entity Type

Business

```html
<!DOCTYPE html>
<html lang="en">
<head>
<meta charset="utf-8">
<title>Zorvex Labs – Business Card</title>
<link rel="stylesheet" href="https://fonts.googleapis.com/css2?family=Open+Sans:wght@400&display=swap">
<style>
  :root {
    --paper: #ffffff;
    --ink: #1a1a1a;
    --ink-soft: #555555;
    --tie-pink: #ec6f9c;
    --tie-lime: #8fc12a;
    --tie-cyan: #21b5d8;
    --tie-red: #e2262b;
    --tie-yellow: #ffe600;
    --tie-orange: #ef7d1a;
    --tie-black: #111111;
  }
  html, body {
    margin: 0;
    padding: 0;
    width: 1200px;
    height: 668px;
    overflow: hidden;
    background: var(--paper);
  }
  .card {
    position: relative;
    width: 1200px;
    height: 668px;
    background: var(--paper);
    font-family: "Open Sans", sans-serif;
    color: var(--ink);
    overflow: hidden;
  }
  .tie-band {
    position: absolute;
    inset: 0;
    width: 1200px;
    height: 668px;
  }
  .holder {
    position: absolute;
    left: 88px;
    top: 78px;
  }
  .holder__name {
    margin: 0;
    font-size: 50px;
    font-weight: 400;
    line-height: 1;
    letter-spacing: -0.5px;
  }
  .holder__role {
    margin: 18px 0 0;
    font-size: 28px;
    color: var(--ink-soft);
    line-height: 1;
  }
  .contact {
    position: absolute;
    left: 88px;
    top: 255px;
    margin: 0;
    padding: 0;
    list-style: none;
    font-size: 29px;
    line-height: 44px;
    color: var(--ink-soft);
  }
  .website {
    position: absolute;
    left: 652px;
    top: 560px;
    margin: 0;
    font-size: 45px;
    line-height: 1;
    color: var(--ink);
  }
</style>
</head>
<body>
  <div class="card">
    <svg class="tie-band" viewBox="0 0 1200 668" role="img" aria-label="Diagonal row of colourful neckties and shirt collars in pink, lime, cyan, red, yellow, orange and black">
      <defs>
        <linearGradient id="tie-band-fill" x1="0" y1="1" x2="1" y2="0">
          <stop offset="0" stop-color="var(--tie-pink)"/>
          <stop offset="0.12" stop-color="var(--tie-lime)"/>
          <stop offset="0.25" stop-color="var(--tie-cyan)"/>
          <stop offset="0.4" stop-color="var(--tie-red)"/>
          <stop offset="0.52" stop-color="var(--tie-yellow)"/>
          <stop offset="0.68" stop-color="var(--tie-orange)"/>
          <stop offset="0.86" stop-color="var(--tie-cyan)"/>
          <stop offset="1" stop-color="var(--tie-pink)"/>
        </linearGradient>
      </defs>
      <polygon points="0,515 1200,118 1200,372 250,668 0,668" fill="url(#tie-band-fill)"/>
    </svg>

    <header class="holder">
      <h1 class="holder__name">Rilan Okoye</h1>
      <p class="holder__role">CEO/Partner</p>
    </header>

    <ul class="contact">
      <li class="contact__email">rilanokoye@zorvexmail.com</li>
      <li class="contact__phone">32 41 70582</li>
      <li class="contact__mobile">8145003716</li>
    </ul>

    <p class="website">www.zorvexlabs.asia</p>
  </div>
</body>
</html>
```